Bread Baking Blog

I need theme modification/customization and logo for a Wordpress theme that I can use the blog about bread baking. Needs to include pictures & recipes.

Can provide access to my quillpage.com site. Have paid for https://plankvault.com/themes/brisk/ but open to alternatives.

The site name is "crumb42.com" (Crumb42 flour is a type of bread flour used in artisan bread baking). Not particular on color palette - am looking for your creativity.

I've included some logos for other domains I have to help provide some inspiration.

```html
<!DOCTYPE html>
<html lang="en">
<head>
<meta charset="utf-8">
<title>Crumb42 — Bread Baking Blog</title>
<link href="https://fonts.googleapis.com/css2?family=Lato:wght@400;700;900&family=Open+Sans:wght@400;600&display=swap" rel="stylesheet">
<style>
:root{
  --accent:#d9822b;
  --gold:#c8923a;
  --gold-light:#f3c23a;
  --brown:#8a6b36;
  --brown-dark:#6f5428;
  --ink:#2b2b2b;
  --muted:#8a8a8a;
  --line:#e6e6e6;
  --paper:#ffffff;
  --tint:#f7f7f7;
}
*{box-sizing:border-box;margin:0;padding:0}
html,body{width:1200px;height:3064px;overflow:hidden;background:var(--paper)}
body{position:relative;font-family:"Open Sans",Arial,sans-serif;color:var(--ink)}
.abs{position:absolute}
h1,h2,h3,h4,.heading{font-family:"Lato",Helvetica,sans-serif}

/* top bar */
.topbar{left:108px;top:8px;width:984px;height:28px;display:flex;justify-content:space-between;align-items:center;font-size:13px;color:#555}
.social{display:flex;gap:12px}
.social span{width:16px;height:16px;border-radius:3px;background:#333;display:block}

/* header */
.brand{left:118px;top:50px;width:110px;height:88px;display:flex;align-items:center;gap:8px}
.brand-dot{width:18px;height:18px;border-radius:50%;background:var(--gold)}
.brand-name{font-family:"Lato",sans-serif;font-weight:900;font-size:24px;color:var(--brown-dark)}
.nav{left:470px;top:68px;height:34px;display:flex;align-items:center;gap:30px;font-size:14px;color:#333}
.nav .caret::after{content:" ▾";font-size:10px}
.btn-recipes{left:980px;top:66px;width:112px;height:36px;border-radius:18px;background:var(--gold);color:#fff;font-size:12px;font-weight:600;display:flex;align-items:center;justify-content:center;letter-spacing:1px}
.rule{left:108px;width:984px;height:1px;background:var(--line)}

/* section headings */
.section-title{font-size:17px;font-weight:900;letter-spacing:.5px;color:#222}
.more-link{font-size:13px;color:var(--accent)}

/* featured */
.featured-card{top:248px;width:228px;height:304px;border-radius:4px;overflow:hidden}
.featured-photo{position:absolute;inset:0;background:linear-gradient(160deg,#6b4a2c,#c9955d 55%,#3a2a1c)}
.featured-caption{position:absolute;left:0;right:0;bottom:0;height:112px;background:rgba(139,103,52,.9);color:#fff;text-align:center;padding:22px 16px 0}
.featured-caption small{display:block;font-size:12px;opacity:.85;margin-bottom:4px}
.featured-caption h3{font-size:15px;font-weight:700;line-height:1.35}
.stars{position:absolute;right:14px;top:14px;display:flex;gap:2px}

/* posts */
.post{left:108px;width:652px;height:320px}
.post-photo{position:absolute;left:0;top:0;width:308px;height:320px;border-radius:3px}
.post-body{position:absolute;left:332px;top:0;width:320px}
.post-meta{font-size:12px;color:var(--muted);margin-bottom:10px}
.post-title{font-size:24px;font-weight:700;color:var(--accent);line-height:1.25;margin-bottom:14px}
.post-excerpt{font-size:13px;line-height:1.65;color:#555;margin-bottom:18px}
.read-more{font-size:13px;color:var(--accent)}

/* sidebar */
.author{left:784px;top:640px;width:308px;text-align:center}
.avatar{width:120px;height:120px;border-radius:50%;margin:0 auto 14px;background:radial-gradient(circle at 50% 40%,#d8c3b0,#8a6c55 70%,#5a4434)}
.author h4{font-size:17px;font-weight:700;margin-bottom:10px}
.author p{font-size:12px;line-height:1.6;color:#555}
.author a{color:var(--accent);text-decoration:none}
.side-heading{left:784px;top:950px;font-size:16px;font-weight:900}
.side-post{left:784px;width:308px;height:60px;display:flex;gap:14px}
.side-thumb{width:88px;height:56px;flex:none;border-radius:2px;background:linear-gradient(135deg,#7a5636,#d2a46c)}
.side-post h5{font-family:"Lato",sans-serif;font-size:13px;font-weight:700;line-height:1.35;margin-bottom:4px}
.side-post small{font-size:11px;color:var(--muted)}
.ad{left:784px;top:1312px;width:308px;height:260px;background:linear-gradient(160deg,#c8151b,#e03a1f 55%,#a50f14)}
.signup{left:784px;top:1620px;width:308px;height:424px;background:linear-gradient(160deg,#e39a2c,#d97f1f);padding:30px 24px;color:#fff}
.signup h4{font-size:20px;font-weight:900;margin-bottom:16px}
.signup p{font-size:12px;line-height:1.6;opacity:.92;margin-bottom:20px}
.field{height:42px;border:1px solid rgba(255,255,255,.6);border-radius:3px;margin-bottom:14px;padding:0 14px;display:flex;align-items:center;font-size:12px;color:rgba(255,255,255,.85)}
.signup-btn{height:46px;border-radius:3px;background:var(--gold-light);color:#7a4a10;font-weight:700;font-size:14px;display:flex;align-items:center;justify-content:center;letter-spacing:1px}

/* pagination */
.pagination{left:0;width:1200px;top:2680px;display:flex;justify-content:center;gap:10px}
.pagination span{width:32px;height:32px;border:1px solid var(--line);border-radius:3px;font-size:13px;display:flex;align-items:center;justify-content:center;color:#555}
.pagination .current{background:var(--accent);border-color:var(--accent);color:#fff}

/* footer */
.footer{left:0;top:2800px;width:1200px;height:208px;background:var(--brown);color:#f3e9d8}
.footer-col{position:absolute;top:36px;width:220px;font-size:12px;line-height:1.75}
.footer-col h4{font-size:14px;font-weight:700;color:#fff;margin-bottom:10px}
.copyright{left:0;top:3008px;width:1200px;height:56px;background:var(--brown-dark);color:#e8dcc6;font-size:12px;display:flex;align-items:center;justify-content:center}
.copyright b{color:#fff;font-weight:600}
</style>
</head>
<body>

<div class="abs topbar"><span>Eat Local Organic Food!</span><div class="social"><span></span><span></span><span></span></div></div>

<div class="abs brand"><span class="brand-dot"></span><span class="brand-name">Crumb42</span></div>
<nav class="abs nav"><span>Home</span><span>Blog</span><span class="caret">Pages</span><span class="caret">Options Panel</span><span>Shop</span>
<svg width="16" height="16" viewBox="0 0 16 16"><circle cx="6.5" cy="6.5" r="5" fill="none" stroke="#333" stroke-width="2"/><line x1="10.5" y1="10.5" x2="15" y2="15" stroke="#333" stroke-width="2"/></svg></nav>
<div class="abs btn-recipes">RECIPES</div>
<div class="abs rule" style="top:160px"></div>

<h2 class="abs section-title" style="left:108px;top:196px">FEATURED</h2>
<span class="abs more-link" style="right:108px;top:198px">View more featured recipes →</span>

<article class="abs featured-card" style="left:108px"><div class="featured-photo" role="img" aria-label="Sourdough loaf on a board"></div>
<div class="stars"><svg width="80" height="14" viewBox="0 0 80 14"><g fill="#f3c23a"><polygon points="7,0 9,5 14,5 10,8 11.5,13 7,10 2.5,13 4,8 0,5 5,5"/><polygon transform="translate(16)" points="7,0 9,5 14,5 10,8 11.5,13 7,10 2.5,13 4,8 0,5 5,5"/><polygon transform="translate(32)" points="7,0 9,5 14,5 10,8 11.5,13 7,10 2.5,13 4,8 0,5 5,5"/><polygon transform="translate(48)" points="7,0 9,5 14,5 10,8 11.5,13 7,10 2.5,13 4,8 0,5 5,5"/><polygon transform="translate(64)" points="7,0 9,5 14,5 10,8 11.5,13 7,10 2.5,13 4,8 0,5 5,5"/></g></svg></div>
<div class="featured-caption"><small>Featured</small><h3>No Knead Sourdough Bread</h3></div></article>
<article class="abs featured-card" style="left:360px"><div class="featured-photo" role="img" aria-label="Whole grain sourdough loaves"></div><div class="featured-caption"><small>Featured</small><h3>Traditional Whole Grain Sourdough</h3></div></article>
<article class="abs featured-card" style="left:612px"><div class="featured-photo" role="img" aria-label="Sliced whole grain loaf"></div><div class="featured-caption"><small>Featured</small><h3>Traditional Whole Grain Sourdough</h3></div></article>
<article class="abs featured-card" style="left:864px"><div class="featured-photo" role="img" aria-label="Dark crusted sourdough loaf"></div><div class="featured-caption"><small>Featured</small><h3>Traditional Whole Grain Sourdough</h3></div></article>

<div class="abs rule" style="top:600px"></div>
<h2 class="abs section-title" style="left:108px;top:644px">LATEST</h2>

<article class="abs post" style="top:704px"><div class="post-photo" role="img" aria-label="Sliced sourdough showing open crumb" style="background:linear-gradient(135deg,#e9d6b8,#b98a58 60%,#6e4d2f)"></div>
<div class="post-body"><div class="post-meta">October 13, 2018 &nbsp;|&nbsp; 0 Comments</div><h3 class="post-title">Sourdough Crumb Structure</h3><p class="post-excerpt">Eaque ipsa quae ab illo inventore veritatis et quasi. Eaque ipsa quae ab illo inventore veritatis et quasi. Ut enim minima veniam quis nostrum exercitationem ullam corporis suscipit laboriosam.</p><span class="read-more">Continue Reading →</span></div></article>

<article class="abs post" style="top:1068px"><div class="post-photo" role="img" aria-label="Whole grain miche loaves on cooling racks" style="background:linear-gradient(135deg,#4a3222,#b07a44 55%,#3b2a1e)"></div>
<div class="post-body"><div class="post-meta">October 13, 2018 &nbsp;|&nbsp; 0 Comments</div><h3 class="post-title">Traditional Whole Grain Miche</h3><p class="post-excerpt">Eaque ipsa quae ab illo inventore veritatis et quasi. Eaque ipsa quae ab illo inventore veritatis et quasi. Ut enim minima veniam quis nostrum exercitationem ullam corporis suscipit laboriosam.</p><span class="read-more">Continue Reading →</span></div></article>

<article class="abs post" style="top:1432px"><div class="post-photo" role="img" aria-label="Seeded loaf beside a seed sack" style="background:linear-gradient(160deg,#3a2a1c,#9c6a3a 50%,#2a2420)"></div>
<div class="post-body"><div class="post-meta">October 13, 2018 &nbsp;|&nbsp; 0 Comments</div><h3 class="post-title">Jory Miller's Seed Feast Loaf</h3><p class="post-excerpt">Lorem ipsum dolor sit amet, consectetur adipiscing elit. Ut tongue, felis dolore sunt. Nibh nunc ingodi. Quorum altera prosunt, nocent altera. Quid ad utilitatem tantae pecuniae ad consequendum more.</p><span class="read-more">Continue Reading →</span></div></article>

<article class="abs post" style="top:1800px"><div class="post-photo" role="img" aria-label="Brown soda bread on a wire rack" style="background:linear-gradient(135deg,#d9d4cc,#8a6a48 55%,#5b4330)"></div>
<div class="post-body"><div class="post-meta">October 13, 2018 &nbsp;|&nbsp; 0 Comments</div><h3 class="post-title">Brown Irish Soda Bread</h3><p class="post-excerpt">Cras a massa viverra, viverra nibh sed, molestie est. Cras semper velit vel euismod interdum. Aenean efficitur scelerisque dolor, eu tempor elit. In hac habitasse platea dictumst. Vivamus tristique libero sapien.</p><span class="read-more">Continue Reading →</span></div></article>

<article class="abs post" style="top:2164px"><div class="post-photo" role="img" aria-label="Sliced homemade French bread" style="background:linear-gradient(135deg,#f3e6c8,#e2b56a 55%,#b67a34)"></div>
<div class="post-body"><div class="post-meta">October 13, 2018 &nbsp;|&nbsp; 0 Comments</div><h3 class="post-title">PERFECT HOMEMADE FRENCH BREAD</h3><p class="post-excerpt">Lorem ipsum dolor sit amet, consectetur adipiscing elit. Ut tongue, felis dolore sunt. Nibh nunc ingodi. Quorum altera prosunt, nocent altera. Quid ad utilitatem tantae pecuniae ad consequendum more.</p><span class="read-more">Continue Reading →</span></div></article>

<aside>
<div class="abs author"><div class="avatar" role="img" aria-label="Author portrait"></div><h4>Mara Lindqvist</h4><p>I'm Mara and I love baking, flour, the yellow colour, but most of all this. <a>Read More »</a></p></div>
<h3 class="abs side-heading">SEE MORE POSTS</h3>
<div class="abs side-post" style="top:1000px"><div class="side-thumb" role="img" aria-label="Bread thumbnail"></div><div><h5>Duis vitae felis tortor nec blandit nec leo</h5><small>Bread Loaves · October 17, 2018</small></div></div>
<div class="abs side-post" style="top:1080px"><div class="side-thumb" role="img" aria-label="Bread thumbnail"></div><div><h5>Consequuntur magni dolores eos qui ratione</h5><small>Bread Loaves · October 17, 2018</small></div></div>
<div class="abs side-post" style="top:1160px"><div class="side-thumb" role="img" aria-label="Bread thumbnail"></div><div><h5>Praesent porta, tortor quis finibus pharetra, tellus</h5><small>Bread Loaves · October 17, 2018</small></div></div>
<div class="abs ad" role="img" aria-label="Advertisement banner with a burger"></div>
<div class="abs signup"><h4>GET MORE STUFF</h4><p>Subscribe to our mailing list and get interesting stuff and updates to your email inbox.</p><div class="field">Enter your name here</div><div class="field">Enter your email here</div><div class="signup-btn">SIGN UP NOW</div></div>
</aside>

<div class="abs pagination"><span class="current">1</span><span>2</span><span>3</span><span>4</span><span>…</span><span>6</span><span>›</span></div>

<footer class="abs footer">
<div class="footer-col" style="left:108px"><h4>About Us</h4>Lorem ipsum dolor sit amet consectetur adipiscing elit. Proin elementum tellus vitae turpis.</div>
<div class="footer-col" style="left:360px"><h4>Archives</h4>October 2018<br>September 2018<br>August 2018<br>July 2018</div>
<div class="footer-col" style="left:612px"><h4>Call Us at</h4>27 Millstone Lane, Dayton, OH<br>Phone: (555) 014 2287<br>hello@crumb42.com</div>
</footer>
<div class="abs copyright"><span><b>Brisk</b> Copyright © 2020 · Theme by <b>PlankVault</b></span></div>

</body>
</html>
```